Bright Arch Group business card

Bright Arch Group is the parent company of Bright Arch Building, Bright Arch Plumbing and Bright Arch Renovating. We require a sophisticated business card that covers all aspects of the building and plumbing space without using told or construction items.

Industry/Entity Type

Construction Company

Contact Information for Business Card

Gareth Pimley
Director
0472915083
gareth@brightarch.com.au
Www.brightarch.com.au

Font styles to use
Serif
Sans Serif

Colors
3176b5
ffce3e
0692cd
34a7d8
fbee3e
faa54b

Requirements
Must have
• Logo on front
• Logo and details on rear.
Nice to have
• Maybe water mark or shadow effect with logo
Should not have
• Tools or any construction associated items

```html
<!DOCTYPE html>
<html lang="en">
<head>
<meta charset="utf-8">
<title>Bright Arch Group – Business Card</title>
<link rel="stylesheet" href="https://fonts.googleapis.com/css2?family=Open+Sans:wght@300;400&display=swap">
<style>
  :root {
    --backdrop: #ece6dc;
    --card-light: #ffffff;
    --card-dark: #131313;
    --ink: #2b2b2b;
    --ink-soft: #444444;
    --accent: #f7861e;
    --logo-light: #e4e4e4;
  }
  * { margin: 0; padding: 0; box-sizing: border-box; }
  html, body { width: 1200px; height: 1200px; overflow: hidden; }
  body {
    background: var(--backdrop);
    font-family: "Open Sans", Arial, sans-serif;
    position: relative;
  }
  .card {
    position: absolute;
    left: 287px;
    width: 626px;
    height: 390px;
    box-shadow: 0 6px 18px rgba(0,0,0,0.12);
  }
  .card--front { top: 150px; background: var(--card-light); }
  .card--back { top: 681px; background: var(--card-dark); }

  .wordmark {
    position: absolute;
    left: 0; right: 0;
    text-align: center;
    font-weight: 300;
    text-transform: uppercase;
    white-space: nowrap;
  }
  .card--front .wordmark {
    top: 86px;
    font-size: 34px;
    letter-spacing: 7px;
    color: var(--ink);
  }
  .card--back .wordmark {
    top: 178px;
    font-size: 40px;
    letter-spacing: 9px;
    color: var(--logo-light);
  }

  .holder {
    position: absolute;
    left: 18px;
    top: 270px;
    padding-left: 13px;
    border-left: 6px solid var(--accent);
  }
  .holder__name {
    font-size: 29px;
    font-weight: 400;
    color: var(--ink-soft);
    line-height: 1.2;
  }
  .holder__role {
    font-size: 18px;
    color: var(--accent);
    line-height: 1.3;
  }

  .contact {
    position: absolute;
    left: 346px;
    top: 264px;
    list-style: none;
  }
  .contact__item {
    display: flex;
    align-items: center;
    height: 32px;
    font-size: 19px;
    color: var(--ink);
  }
  .contact__icon {
    width: 18px;
    height: 18px;
    margin-right: 11px;
    flex: none;
  }
</style>
</head>
<body>
  <section class="card card--front" aria-label="Card front">
    <div class="wordmark">Bright Arch Group</div>

    <div class="holder">
      <div class="holder__name">Gareth Pimley</div>
      <div class="holder__role">Director</div>
    </div>

    <ul class="contact">
      <li class="contact__item">
        <svg class="contact__icon" viewBox="0 0 20 20" aria-hidden="true">
          <path d="M2 8c0-3 4-5 8-5s8 2 8 5l-3 1-1-2H6L5 9z" fill="var(--accent)"/>
          <rect x="4" y="10" width="12" height="7" rx="1.5" fill="var(--accent)"/>
          <circle cx="10" cy="13.5" r="2" fill="#fff"/>
        </svg>
        0472915083
      </li>
      <li class="contact__item">
        <svg class="contact__icon" viewBox="0 0 20 20" aria-hidden="true">
          <rect x="1" y="5" width="18" height="11" fill="var(--accent)"/>
          <path d="M1 5l9 6 9-6M1 16l7-5M19 16l-7-5" stroke="#fff" stroke-width="1.3" fill="none"/>
        </svg>
        gareth@brightarch.com.au
      </li>
      <li class="contact__item">
        <svg class="contact__icon" viewBox="0 0 20 20" aria-hidden="true">
          <g fill="none" stroke="var(--accent)" stroke-width="1.3">
            <circle cx="10" cy="10" r="8"/>
            <ellipse cx="10" cy="10" rx="3.5" ry="8"/>
            <path d="M2 10h16M3.5 6h13M3.5 14h13"/>
          </g>
        </svg>
        Www.brightarch.com.au
      </li>
    </ul>
  </section>

  <section class="card card--back" aria-label="Card back">
    <div class="wordmark">Bright Arch Group</div>
  </section>
</body>
</html>
```